Book Cover : Silent Tides: Protein Engines and the Cellular Horizon

We need a striking and engaging book cover for this new book which describes the development of the COVID-19 vaccine technology and it's potential to change the world in ways which most people don't yet realise.

On the book cover we need to include:

Silent Tides: Protein Engines and the Cellular Horizon

Safety/Efficiency/Future Applications/CRISPR

Tadeusz Głowik

Need extra days to review

```html
<!DOCTYPE html>
<html lang="en">
<head>
<meta charset="utf-8">
<title>Silent Tides: Protein Engines and the Cellular Horizon — Book Cover</title>
<link rel="stylesheet" href="https://fonts.googleapis.com/css2?family=Montserrat:wght@400;700&display=swap">
<style>
  :root {
    --page-bg: #ffffff;
    --cover-orange: #e08c26;
    --cover-green: #3e8e44;
    --ink-dark: #231f20;
    --ink-light: #ffffff;
    --art-tint: rgba(255, 255, 255, 0.16);
    --art-edge: rgba(255, 255, 255, 0.55);
  }
  * { margin: 0; padding: 0; box-sizing: border-box; }
  html, body {
    width: 1200px;
    height: 1200px;
    overflow: hidden;
    background: var(--page-bg);
  }
  .canvas {
    position: relative;
    width: 1200px;
    height: 1200px;
    font-family: "Montserrat", Arial, sans-serif;
  }
  .book-cover {
    position: absolute;
    left: 360px;
    top: 240px;
    width: 480px;
    height: 720px;
    overflow: hidden;
  }
  .title-band {
    position: absolute;
    left: 0; top: 0;
    width: 480px;
    height: 330px;
    background: var(--cover-orange);
  }
  .topics-band {
    position: absolute;
    left: 0; top: 330px;
    width: 480px;
    height: 390px;
    background: var(--cover-green);
  }
  .title-main {
    position: absolute;
    left: 20px;
    top: 88px;
    color: var(--ink-dark);
    font-weight: 700;
    font-size: 47px;
    line-height: 56px;
  }
  .title-sub {
    position: absolute;
    left: 20px;
    top: 230px;
    color: var(--ink-dark);
    font-weight: 400;
    font-size: 26px;
    line-height: 33px;
    letter-spacing: 0.3px;
  }
  .vial-art {
    position: absolute;
    left: 257px;
    top: 47px;
    width: 200px;
    height: 172px;
    border-radius: 14px 14px 10px 10px;
    background: radial-gradient(ellipse at 45% 55%, var(--art-tint), rgba(255,255,255,0.05));
    border: 2px solid var(--art-edge);
  }
  .syringe-art {
    position: absolute;
    left: 73px;
    top: 27px;
    width: 43px;
    height: 336px;
    border-radius: 8px;
    background: linear-gradient(180deg, rgba(255,255,255,0.08), var(--art-tint));
    border: 2px solid var(--art-edge);
  }
  .topic-list {
    position: absolute;
    left: 126px;
    top: 58px;
    list-style: none;
    color: var(--ink-light);
    font-weight: 700;
    font-size: 25px;
    line-height: 33.5px;
  }
  .author-name {
    position: absolute;
    left: 126px;
    top: 314px;
    color: var(--ink-light);
    font-weight: 400;
    font-size: 28px;
    line-height: 34px;
    letter-spacing: 0.3px;
  }
</style>
</head>
<body>
  <div class="canvas">
    <div class="book-cover">
      <section class="title-band">
        <h1 class="title-main">Silent<br>Tides:</h1>
        <p class="title-sub">Protein Engines and the<br>Cellular Horizon</p>
        <div class="vial-art" role="img" aria-label="White line illustration of a labelled vaccine vial with its round cap lying beside it"></div>
      </section>
      <section class="topics-band">
        <div class="syringe-art" role="img" aria-label="White line illustration of a vertical syringe with needle pointing up"></div>
        <ul class="topic-list">
          <li>Safety</li>
          <li>Efficiency</li>
          <li>Future Applications</li>
          <li>CRISPR</li>
        </ul>
        <p class="author-name">Tadeusz Głowik</p>
      </section>
    </div>
  </div>
</body>
</html>
```